Business Card Design Project

We need a business card for a chiropractic and rehabilitation center. We already have a logo and need the card to follow the color and feel of the logo.

Target Market(s)

adults 30-55 that have some ache or pain that is interfering with their life, so much as they are ready to do something about it.

Industry/Entity Type

Business

```html
<!DOCTYPE html>
<html lang="en">
<head>
<meta charset="utf-8">
<title>CorePath Business Card</title>
<link href="https://fonts.googleapis.com/css2?family=Open+Sans:wght@400;600;700&display=swap" rel="stylesheet">
<style>
  :root {
    --stage: #e9ebec;
    --card: #ffffff;
    --ink: #333333;
    --ink-soft: #555555;
    --brand-gray: #58595b;
    --band-orange: #f7982a;
    --rule-gray: #4a4a4c;
  }
  * { margin: 0; padding: 0; box-sizing: border-box; }
  html, body {
    width: 987px;
    height: 1200px;
    overflow: hidden;
    background: var(--stage);
    font-family: "Open Sans", Arial, sans-serif;
    color: var(--ink);
  }
  .card {
    position: absolute;
    width: 788px;
    height: 450px;
    background: var(--card);
    border-radius: 24px;
    overflow: hidden;
  }
  .card--front { left: 92px; top: 88px; }
  .card--back  { left: 94px; top: 627px; }

  .brand {
    position: absolute;
    font-weight: 600;
    color: var(--brand-gray);
    line-height: 1;
    white-space: nowrap;
  }
  .card--front .brand { left: 46px; top: 84px; font-size: 62px; }
  .card--back .brand { left: 0; right: 0; top: 160px; text-align: center; font-size: 86px; }

  .contact {
    position: absolute;
    left: 408px;
    top: 84px;
  }
  .contact__name { font-size: 26px; font-weight: 700; color: var(--ink); line-height: 1.1; }
  .contact__title { font-size: 16px; color: var(--ink-soft); margin-left: 11px; margin-top: 4px; }
  .contact__list { list-style: none; margin-top: 14px; }
  .contact__item {
    display: flex;
    align-items: center;
    gap: 8px;
    font-size: 19px;
    color: var(--ink);
    height: 41px;
  }
  .contact__icon { width: 18px; height: 18px; fill: var(--ink); flex: none; }

  .band { position: absolute; left: 0; top: 0; width: 788px; height: 450px; }

  .address {
    position: absolute;
    left: 44px;
    top: 374px;
    font-size: 20px;
    line-height: 29px;
    color: #222222;
    font-style: normal;
  }
  .website {
    position: absolute;
    left: 0; right: 0;
    top: 354px;
    text-align: center;
    font-size: 32px;
    color: var(--ink);
  }
</style>
</head>
<body>

<section class="card card--front">
  <svg class="band" viewBox="0 0 788 450" aria-hidden="true">
    <path d="M0,318 Q394,360 788,430 L788,450 L0,450 Z" fill="var(--band-orange)"/>
    <path d="M0,306 Q394,348 788,418" fill="none" stroke="var(--rule-gray)" stroke-width="3"/>
  </svg>

  <div class="brand">CorePath</div>

  <div class="contact">
    <p class="contact__name">Marcus Ellery,</p>
    <p class="contact__title">D.C., C.E.S</p>
    <ul class="contact__list">
      <li class="contact__item">
        <svg class="contact__icon" viewBox="0 0 24 24" aria-hidden="true"><path d="M3 8c0-3 4-4 9-4s9 1 9 4v2h-5V8H8v2H3z M6 12h12l2 8H4z"/></svg>
        512-555-0148
      </li>
      <li class="contact__item">
        <svg class="contact__icon" viewBox="0 0 24 24" aria-hidden="true"><text x="2" y="19" font-size="20" font-weight="700" font-family="Open Sans, sans-serif">@</text></svg>
        drmellery@corepath-wellness.com
      </li>
      <li class="contact__item">
        <svg class="contact__icon" viewBox="0 0 24 24" aria-hidden="true"><circle cx="12" cy="12" r="9"/><path d="M3 12h18M12 3c-4 4-4 14 0 18M12 3c4 4 4 14 0 18" stroke="#fff" stroke-width="1.5" fill="none"/></svg>
        www.corepath-wellness.com
      </li>
    </ul>
  </div>

  <address class="address">
    2740 W Briarcliff Ln<br>
    Ste 204, Austin TX 78745
  </address>
</section>

<section class="card card--back">
  <div class="brand">CorePath</div>
  <p class="website">www.website.com</p>
</section>

</body>
</html>
```